Book Cover Design - Uncovering Weight Loss Secrets

I need a book cover design for a book called 'Folding The Map'. It is a book that goes through all of the secrets to weight loss, without any crazy shakes or workouts or pills or potions. The book is really focused on helping people understand that Weight loss is simple and has more to do with our mindset as well as the food we were eating. It is about taking personal responsibility not looking for the next fancy revolutionary product that is going to help them magically melt the fat away. The book is pragmatic in nature and breaks down in simple terms how we can lose weight and keep it off for the rest of our lives. It shows the user that it is simple to lose weight, but it takes effort. They should stop looking for a quick fix when it comes to weight loss but instead eat healthy for the rest of their lives.
The book is intended to be hard-hitting no holds barred approach. The book has the same title as my business name. I will attach the current logo that we use in the business. This doesn't need to be on the front of the book maybe at the back down the bottom somewhere.
I am looking to have both an e-book cover and a standard printed book cover.
I don't have any colours in mind, my logo can be adapted to be different colours or just white.
The message that I am wanting people to feel when they see my book, is that all these Weightloss fads are a joke, that I know the secrets that will get them to their weight loss goal even if they fail at everything else before.
On the cover it should say the following.
FOLDING THE MAP
Uncovering the Weight Loss Secrets
The big companies have been trying to keep hidden for years!
COLIN MAYHEW
People who have failed many times trying to lose weight & need help
Weight Loss

```html
<!DOCTYPE html>
<html lang="en">
<head>
<meta charset="utf-8">
<title>Folding The Map – Book Cover</title>
<link rel="stylesheet" href="https://fonts.googleapis.com/css2?family=Barlow:wght@700&family=Barlow+Condensed:wght@300;400;600&display=swap">
<style>
  :root {
    --backdrop: #e4e4e4;
    --cover: #ffffff;
    --ink: #262a27;
    --orange: #f07a2a;
    --green: #5fa83c;
    --red: #e8343c;
    --blue: #4a67a8;
    --taupe: #a88c72;
    --lock: #ffffff;
  }
  html, body {
    margin: 0;
    width: 1200px;
    height: 1188px;
    overflow: hidden;
    background: var(--backdrop);
  }
  .book-cover {
    position: absolute;
    left: 233px;
    top: 44px;
    width: 734px;
    height: 1100px;
    background: var(--cover);
    color: var(--ink);
    text-align: center;
  }
  .book-title {
    position: absolute;
    top: 70px;
    left: 0;
    width: 100%;
    margin: 0;
    font-family: "Barlow", sans-serif;
    font-weight: 700;
    font-size: 128px;
    line-height: 110px;
    letter-spacing: -1px;
  }
  .book-subtitle {
    position: absolute;
    top: 314px;
    left: 0;
    width: 100%;
    margin: 0;
    font-family: "Barlow Condensed", sans-serif;
    font-weight: 300;
    font-size: 28px;
    line-height: 32px;
  }
  .book-subtitle strong {
    font-weight: 600;
  }
  .cover-illustration {
    position: absolute;
    left: 148px;
    top: 420px;
    width: 500px;
    height: 540px;
  }
  .book-author {
    position: absolute;
    top: 1008px;
    left: 0;
    width: 100%;
    margin: 0;
    font-family: "Barlow Condensed", sans-serif;
    font-weight: 400;
    font-size: 34px;
    letter-spacing: 0.7em;
    text-indent: 0.7em;
  }
</style>
</head>
<body>
  <main class="book-cover">
    <h1 class="book-title">FOLDING<br>THE MAP</h1>
    <p class="book-subtitle"><strong>Uncovering the Weight Loss Secrets</strong> the big<br>companies have been trying to keep hidden for years!</p>

    <svg class="cover-illustration" viewBox="0 0 500 540" role="img" aria-label="Illustration area: a colourful low-poly brain seen from above, split into two halves, with a white padlock at its centre">
      <defs>
        <linearGradient id="illustration-tones" x1="0" y1="0" x2="0.4" y2="1">
          <stop offset="0" stop-color="var(--orange)"/>
          <stop offset="0.3" stop-color="var(--green)"/>
          <stop offset="0.6" stop-color="var(--red)"/>
          <stop offset="1" stop-color="var(--blue)"/>
        </linearGradient>
      </defs>
      <rect class="illustration-placeholder" x="0" y="0" width="500" height="540" rx="24" fill="url(#illustration-tones)" opacity="0.85"/>
      <g class="padlock-icon">
        <path d="M196 212 V180 A54 54 0 0 1 304 180 V212" fill="none" stroke="var(--lock)" stroke-width="26"/>
        <rect x="164" y="210" width="172" height="148" fill="var(--lock)"/>
        <circle cx="250" cy="268" r="16" fill="var(--green)"/>
        <path d="M243 276 H257 L262 322 H238 Z" fill="var(--green)"/>
      </g>
    </svg>

    <p class="book-author">COLIN MAYHEW</p>
  </main>
</body>
</html>
```